Retail and Ecommerce Archery Shop needs new Home Page Design

We need a homepage design created for an existing company named Harlow Ridge Sport Depot. They sell various types of Archery equipment for both Bow hunting and Target shooting both in store and online. They offer shooting lessons, have an indoor archery shooting range with memberships available, and have their own line of bowstrings. For color scheme, use the current home page as inspiration. The Homepage Template has links to specific images, if any other images are needed, stock images are acceptable.

Current Website: https://hrsportdepot.com/

Customer Avatar: https://files.norvexa.com/doc/d/7Tq2Wm9XbR4LpZ8vKc3NhY6JfG1sDe5AaUoPiQwErTy/view?mode=share

Core Message Canvas: https://files.norvexa.com/sheet/d/4K_718bnRz962T3w57nLqX8hjd4Mc2Vb7wP0gE3R_uHz/view?mode=share

Homepage Template-Use this worksheet as the structue of the homepage: https://files.norvexa.com/doc/d/9pLxTrWq2N8mHc4ZbVs5KdYo7GfEjU3RaCiAwB6nMeQ/view?mode=share

```html
<!DOCTYPE html>
<html lang="en">
<head>
<meta charset="utf-8">
<title>Harlow Ridge Sport Depot — Home</title>
<link href="https://fonts.googleapis.com/css2?family=Libre+Baskerville:wght@400;700&family=Inter:wght@400;500;600;700&display=swap" rel="stylesheet">
<style>
:root{
  --red:#ed1c24;
  --blue:#0a86d0;
  --navy:#1b4c6f;
  --dark:#222222;
  --footer:#2b2b2b;
  --ink:#1a1a1a;
  --muted:#555;
  --light:#f7f7f7;
  --white:#fff;
}
*{margin:0;padding:0;box-sizing:border-box}
html,body{width:1200px;height:4508px;overflow:hidden}
body{font-family:"Inter",Arial,sans-serif;color:var(--ink);background:var(--white);position:relative}
.serif{font-family:"Libre Baskerville",Georgia,serif}
.abs{position:absolute}

.topbar{top:0;left:0;width:1200px;height:49px;background:var(--dark);color:#fff;font-size:10px;letter-spacing:.3px;display:flex;align-items:center;justify-content:center}
.nav{top:49px;left:0;width:1200px;height:68px;background:#fff;display:flex;align-items:center;padding:0 124px;font-size:10px;text-transform:uppercase;color:#333}
.nav a{margin-right:42px;color:#333;text-decoration:none}
.nav .icons{margin-left:auto;display:flex;gap:14px}
.nav .icons span{width:30px;height:30px;border-radius:50%;background:var(--red);display:flex;align-items:center;justify-content:center}

.hero{top:117px;left:0;width:1200px;height:674px;background:linear-gradient(110deg,#1a1d14 0%,#3a3b2c 40%,#6f6a55 70%,#4a4a5a 100%)}
.brand{color:#f2c21a;font-family:"Libre Baskerville",Georgia,serif;font-weight:700;font-size:19px;line-height:1.2;display:flex;align-items:center;gap:8px}
.brand i{width:14px;height:14px;border-radius:50%;background:var(--red);display:inline-block}
.hero h1{top:215px;left:124px;width:560px;color:#fff;font-size:44px;line-height:58px;font-weight:400}
.hero .tag{top:414px;left:124px;color:#fff;font-size:13px;letter-spacing:.2px}
.btn{display:flex;align-items:center;justify-content:space-between;color:#fff;font-size:11px;font-weight:500;text-transform:uppercase;padding:0 20px;height:42px}
.btn::after{content:"";width:2px;height:20px;background:#fff}
.btn-red{background:var(--red)}
.btn-blue{background:var(--blue)}

.services h2{top:885px;left:0;width:1200px;text-align:center;font-size:34px;line-height:46px;font-weight:400}
.tile{width:303px;height:280px;display:flex;align-items:center;justify-content:center;color:#fff;font-family:"Libre Baskerville",Georgia,serif;font-weight:700;font-size:26px;letter-spacing:1px}
.tile.t1{background:#1e1a1a}.tile.t2{background:#2c2c2c}.tile.t3{background:#141414}.tile.t5{background:#262a26}.tile.t6{background:#3a3a3a}
.tile.info{background:var(--blue);font-family:"Inter",Arial,sans-serif;font-weight:400;font-size:15px;line-height:20px;letter-spacing:0;align-items:flex-start;justify-content:flex-start;padding:40px 32px}

.bowstrings{top:1706px;left:0;width:1200px;height:583px;background:var(--blue)}
.bowstrings .redcol{position:absolute;top:0;left:751px;width:449px;height:583px;background:var(--red);padding:14px 14px 0 22px;color:rgba(255,255,255,.18);font-size:14px;line-height:20.5px;text-align:justify;overflow:hidden}
.bowstrings h2{position:absolute;top:180px;left:124px;color:#fff;font-size:36px;line-height:48px;font-weight:400}
.device{position:absolute;top:82px;left:479px;width:595px;height:423px;background:#f4f4f4;border-radius:22px;border:1px solid #ddd;box-shadow:0 6px 20px rgba(0,0,0,.25)}
.device .screen{position:absolute;top:24px;left:51px;width:495px;height:373px;background:linear-gradient(120deg,#3e5a3a,#6c7c55 50%,#2b3a2a);border:1px solid #111}
.device .play{position:absolute;top:50%;left:50%;transform:translate(-50%,-50%)}

.welcome h2{top:2380px;left:0;width:1200px;text-align:center;font-size:38px;line-height:50px;font-weight:400}
.welcome .bar{top:2499px;left:340px;width:519px;height:49px;background:var(--red);color:#fff;font-weight:700;font-size:15px;display:flex;align-items:center;justify-content:center}
.photo{background:linear-gradient(140deg,#1c2230,#4a4f5e 55%,#2a2f3c)}
.welcome h3{top:3004px;left:0;width:1200px;text-align:center;font-size:23px;line-height:31px;font-weight:700}
.welcome p{top:3094px;left:310px;width:580px;text-align:center;font-size:11.5px;line-height:15px;color:#333}

.community{top:3238px;left:0;width:1200px;height:654px;background:var(--light)}
.community h2{position:absolute;top:240px;left:124px;font-size:34px;line-height:48px;font-weight:400}
.community p{position:absolute;top:358px;left:124px;width:440px;font-size:18px;line-height:23px;color:#333}
.card-shadow{position:absolute;top:114px;left:654px;width:428px;height:460px;background:var(--red)}
.card{position:absolute;top:98px;left:646px;width:428px;height:466px;background:#fff;padding:122px 32px 0;text-align:center}
.card h4{font-family:"Libre Baskerville",Georgia,serif;font-size:15px;line-height:23px;font-weight:700;margin-bottom:24px}
.field{width:358px;height:40px;border:1px solid #ddd;background:#f6f6f6;text-align:left;font-size:11px;color:#999;padding:12px 20px;margin:0 auto 15px}
.card .btn{width:286px;margin:0 auto;height:40px}

.footer{top:3892px;left:0;width:1200px;height:616px;background:var(--footer);color:#fff}
.footer .brand{position:absolute;top:108px;left:0;width:1200px;justify-content:center;font-size:24px}
.footer .about{position:absolute;top:212px;left:300px;width:600px;text-align:center;font-size:12px;line-height:18px}
.footer .links{position:absolute;top:301px;left:124px;width:952px;height:56px;background:var(--navy);display:flex;align-items:center;padding-left:124px;gap:80px;font-size:12px;text-transform:uppercase}
.contact{position:absolute;top:388px;display:flex;gap:18px;font-size:11.5px;line-height:18px}
.contact small{display:block;font-size:8px;text-transform:uppercase;opacity:.8}
.footer .rule{position:absolute;top:553px;left:124px;width:952px;height:1px;background:#666}
.footer .copy{position:absolute;top:575px;left:0;width:1200px;text-align:center;font-size:11px}
</style>
</head>
<body>

<div class="abs topbar">NEW REWARDS PROGRAM IN EFFECT! START EARNING POINTS TO REDEEM ON PURCHASES! CURRENT LEAD TIME ON STRINGS: 3 WEEKS</div>

<nav class="abs nav">
  <a>Home</a><a>About ▾</a><a>Electric Bowstrings</a><a>Pro Shop</a><a>Range</a><a>Shop ▾</a>
  <div class="icons">
    <span><svg width="13" height="13" viewBox="0 0 14 14"><circle cx="6" cy="6" r="4.5" fill="none" stroke="#fff" stroke-width="2"/><line x1="9.5" y1="9.5" x2="13" y2="13" stroke="#fff" stroke-width="2"/></svg></span>
    <span><svg width="13" height="13" viewBox="0 0 14 14"><rect x="2" y="5" width="10" height="8" rx="1" fill="#fff"/><path d="M4.5 5V4a2.5 2.5 0 0 1 5 0v1" fill="none" stroke="#fff" stroke-width="1.5"/></svg></span>
  </div>
</nav>

<section class="abs hero" role="img" aria-label="Bow hunter in camouflage drawing a compound bow among wildflowers">
  <div class="abs brand" style="top:48px;left:124px"><i></i>Harlow Ridge<br>Sport Depot</div>
  <h1 class="abs serif">YOUR BOW HUNTING ADVENTURE STARTS HERE!</h1>
  <div class="abs tag">TOP-NOTCH EQUIPMENT • EXPERTISE • UNMATCHED SUPPORT</div>
  <div class="abs btn btn-red" style="top:465px;left:124px;width:265px">Indoor Archery Range</div>
  <div class="abs btn btn-blue" style="top:465px;left:404px;width:265px">Shop Our Bows</div>
</section>

<section class="services">
  <h2 class="abs serif">WE ARE A FULL-SERVICE ARCHERY<br>PRO SHOP</h2>
  <div class="abs tile t1" style="top:1027px;left:124px" role="img" aria-label="Archery brand tile">Vantor</div>
  <div class="abs tile t2" style="top:1027px;left:448px" role="img" aria-label="Archery brand tile">Marlen</div>
  <div class="abs tile t3" style="top:1027px;left:772px" role="img" aria-label="Archery brand tile">Hexa</div>
  <div class="abs tile info" style="top:1328px;left:124px">Our services include Bow setup and sizing, D-loop and peep sight installs, accessory installs, and setup, cam/limb swaps, string swaps, paper tuning, 2nd/3rd axis adjustments, replacement parts, arrow building, tuning, and much more!</div>
  <div class="abs tile t5" style="top:1328px;left:448px" role="img" aria-label="Archery brand tile">Brightline</div>
  <div class="abs tile t6" style="top:1328px;left:772px" role="img" aria-label="Archery brand tile">Ellio</div>
</section>

<section class="abs bowstrings">
  <div class="redcol">Lorem Ipsum is simply dummy text of the printing and typesetting industry. Lorem Ipsum has been the industry's standard dummy text ever since the 1500s, when an unknown printer took a galley of type and scrambled it to make a type specimen book. It has survived not only five centuries, but also the leap into electronic typesetting, remaining essentially unchanged. It was popularised in the 1960s with the release of sheets containing passages, and more recently with desktop publishing software like versions of Lorem Ipsum. Lorem Ipsum is simply dummy text of the printing and typesetting industry. Lorem Ipsum has been the industry's standard dummy text ever since the 1500s, when an unknown printer took a galley of type and scrambled it to make a type specimen book. It has survived not only five centuries, but also the leap into electronic typesetting, remaining essentially unchanged. Lorem Ipsum has been the industry's standard dummy text ever since the 1500s, when an unknown printer took a galley of type and scrambled it to make a type specimen.</div>
  <h2 class="serif">OUR CUSTOM<br>ELECTRIC<br>BOWSTRINGS</h2>
  <div class="abs btn btn-red" style="top:358px;left:124px;width:298px">Shop Our Custom Bowstrings</div>
  <div class="device">
    <div class="screen" role="img" aria-label="Video still of an archer aiming a compound bow">
      <svg class="play" width="80" height="80" viewBox="0 0 80 80"><circle cx="40" cy="40" r="36" fill="none" stroke="#fff" stroke-width="4"/><path d="M32 24 L58 40 L32 56Z" fill="#fff"/></svg>
    </div>
  </div>
</section>

<section class="welcome">
  <h2 class="abs serif">WELCOME TO YOUR LOCAL<br>ARCHERY SHOP</h2>
  <div class="abs bar">WHERE CONSISTENCY IS BUILT</div>
  <div class="abs photo" style="top:2620px;left:0;width:266px;height:327px" role="img" aria-label="Customer viewing bows on a display wall"></div>
  <div class="abs photo" style="top:2599px;left:287px;width:626px;height:369px" role="img" aria-label="Shop staff talking with customers at an archery expo booth"></div>
  <div class="abs photo" style="top:2620px;left:934px;width:266px;height:327px" role="img" aria-label="Busy archery trade show floor"></div>
  <h3 class="abs serif">LOOKING TO MAKE SOME IMPROVEMENTS TO<br>YOUR CURRENT ARCHERY SETUP?</h3>
  <p class="abs">We have access to almost all of the popular archery accessories on the market! We don't sell anything we wouldn't use ourselves so come on in and talk with our shop experts to figure out what will work best for you.</p>
</section>

<section class="abs community">
  <h2 class="serif">JOIN OUR ARCHERY<br>COMMUNITY:</h2>
  <p>Join today &amp; stay up-to-date on new product releases, shop promotions, and our archery newsletters</p>
  <div class="card-shadow"></div>
  <div class="card">
    <h4>EXCLUSIVE DEALS, TIPS, AND UPDATES<br>STRAIGHT TO YOUR INBOX!</h4>
    <div class="field">Name</div>
    <div class="field">Email</div>
    <div class="btn btn-blue">Subscribe</div>
  </div>
</section>

<footer class="abs footer">
  <div class="brand"><i></i>Harlow Ridge Sport Depot</div>
  <p class="about">Lorem Ipsum is simply dummy text of the printing and typesetting industry. Lorem Ipsum has been the industry's standard dummy text ever since the 1500s.</p>
  <div class="links"><span>Shop</span><span>About Us</span><span>Range</span><span>Pro Shop</span><span>Electric Bowstrings</span></div>
  <div class="contact" style="left:124px;top:410px">
    <svg width="22" height="16" viewBox="0 0 22 16"><rect width="22" height="16" rx="2" fill="#fff"/><path d="M1 2 L11 9 L21 2" fill="none" stroke="#2b2b2b" stroke-width="1.6"/></svg>
    <div><small>Mail</small>hello@harlowridgedepot.com</div>
  </div>
  <div class="contact" style="left:500px;top:388px">
    <svg width="20" height="20" viewBox="0 0 20 20"><path d="M19 1 L1 9 L9 11 L11 19Z" fill="#fff"/></svg>
    <div><small>Address</small>Unit 12 Fenwick Court<br>Marlow Trade Park Westgate<br>Road Harlow HR4 2LQ</div>
  </div>
  <div class="contact" style="left:906px;top:410px">
    <svg width="22" height="22" viewBox="0 0 24 24"><path d="M6.6 10.8a15 15 0 0 0 6.6 6.6l2.2-2.2a1 1 0 0 1 1-.25 11.4 11.4 0 0 0 3.6.57 1 1 0 0 1 1 1V20a1 1 0 0 1-1 1A17 17 0 0 1 3 4a1 1 0 0 1 1-1h3.5a1 1 0 0 1 1 1c0 1.25.2 2.45.57 3.57a1 1 0 0 1-.25 1Z" fill="#fff"/></svg>
    <div><small>Phone</small>+44 (0)155 204 3391</div>
  </div>
  <div class="rule"></div>
  <div class="copy">© Copyright © 2023 Harlow Ridge Holdings. All Rights Reserved-Terms Of Service-Privacy Policy</div>
</footer>

</body>
</html>
```